依頼詳細
<現状サイトの課題>
①一目で、何をしている会社なのかが分からない。
⇒商品画像・作業画像などを入れ、分かりやすく目を引き付けるようにする。

②項目が小さく、引き付けにくいデザイン。
⇒アイコンを大きくして、デザイン性を持たせる。

③自社の強みを視覚化できていない。
⇒図や写真を追加し、視覚的に伝わるようにする。

④自社の新着情報がないので社内の動きが把握できない。
⇒新着ニュースを追加し社内の動きが把握できるようにする。

⑤企業規模が小さく感じてしまう。
⇒洗練されたデザイン、コンテンツの充実、グローバルサイトの作成により企業規模をワンランク大きく見えるように表現する。
----------------------------------
<現在のサイト>
明確なサイトの情報共有はできませんが、TOPページの情報を一部伏せて共有します。添付の”TOPページ”をご参照ください。

<サイトリニューアルの方針>
①強みを明確にする為、全体的に画像化し打ち出したい。TOPページは動画を掲載し、よりリアルにユーザー様にイメージが伝わるデザインにする。

②企業規模をワンランク大きく見えるように表現し、グローバル化についてもアピールすることで、事業規模の大きい信頼出来る会社であることが分かるようにし、新規顧客の獲得および定着するようにサイトリニューアルを行う。

③必須機能
・TOPページへ動画を埋め込む。
・スマホ対応(レスポンシブウェブデザイン)にする。
・ウェブ見積り機能を設け、いつでも見積りが確認できるようにする。(TOPページにバナーを設けるなどデザインする)

<イメージ参考サイト>
①メインカラーをブルーとし、TOPページを開くとすぐに大きな画像イメージが見えます。
https://www.e-hariwa.co.jp/

②トップページに表示される、動画イメージです。
https://www.dovel.co.jp/

③コンテンツの配置や施工事例が見やすいです。
http://www.tasemi-kk.com/

④TOPページに施工写真や文字が挿入されており分かりやすい。また企業イメージがよく考えられており、ブランディングされています。
http://www.fujiyaga.co.jp/

<カラーテーマ>
①青系(堅実・信頼・クール)または水色系(さわやか・清潔感)

②青4割、白6割の配色のイメージでお願いします。制作の際は、カラーチャート(カラーを選んだ理由)もご提示いただけると幸いです。

<重視する点/検討基準>
①サイトコンセプトにあったデザイン(ご提案の際は、制作頂いたデザインコンセプト及びデザイン説明コメントの記載をお願い致します)

②納期厳守

<具体的な制作数>
TOPページ:1ページ(PC版のデザイン制作をお願いします)

<選考の進め方>
ご提案頂いたデザイン内容・コンセプトなどをもとに、プロジェクトメンバーで選考、決定致します。
※今回は、トップページデザインのみの見積りとなります。
今後、コーディングを依頼する可能性もございます。その場合は改めてクリエタスを通じてご依頼させて頂きます。パララックスデザインでのコーディングも条件として入れてまいります。
1ページ
青系、水色系
• イラストレーター形式 (.ai)
• フォトショップ形式 (.psd)
追記です。
サイトコンセプトの資料も添付いたします。
宜しくお願いいたします。

クライアント様と協議させていただき、コンセプトに合った総合的なデザインを評価させて頂きました。
その中で、クライアント様からの評価が多かった「Pixfern様」を当選とさせていただきました。ありがとうございました。

ランサーの皆さん、このように沢山の素敵なデザインをご提案頂き本当にありがとうございました。
コンセプトを基に、クライアント様とも大いに悩んで決定させて頂きました。
また、選定が期限間近になってしまいましたこと、申し訳ございませんでした。

機会があれば、今後ともどうぞ宜しくお願い致します。

```html
<!DOCTYPE html>
<html lang="ja">
<head>
<meta charset="utf-8">
<title>鉄骨階段製作 トップページ</title>
<link rel="stylesheet" href="https://fonts.googleapis.com/css2?family=Noto+Sans+JP:wght@400;500;700&display=swap">
<style>
:root{
  --navy:#1f3f6b;
  --blue:#3a5f8f;
  --steel:#6f87a6;
  --pale:#e9eef4;
  --gray:#eef0f2;
  --line:#c9d3df;
  --red:#d8362b;
  --text:#333a44;
  --muted:#6a7482;
  --white:#ffffff;
}
*{box-sizing:border-box;margin:0;padding:0}
html,body{width:1200px;height:3316px;overflow:hidden}
body{font-family:"Noto Sans JP",sans-serif;color:var(--text);background:var(--white);position:relative}
.abs{position:absolute}

/* header */
.site-header{position:absolute;left:0;top:0;width:1200px;height:170px;background:rgba(255,255,255,.88);z-index:3}
.brand{position:absolute;left:560px;top:0;width:80px;height:62px;background:var(--navy);display:flex;align-items:center;justify-content:center}
.brand span{color:#fff;font-size:13px;font-weight:500;letter-spacing:.05em}
.brand-sub{position:absolute;left:560px;top:66px;width:80px;text-align:center;font-size:10px;color:var(--steel)}
.tel{position:absolute;left:812px;top:40px;font-size:26px;font-weight:700;color:var(--red);letter-spacing:.04em}
.global-nav{position:absolute;left:250px;top:104px;width:700px;display:flex;justify-content:space-between}
.global-nav a{width:80px;text-align:center;text-decoration:none;color:var(--navy);font-size:11px;font-weight:500}
.global-nav svg{display:block;margin:0 auto 6px;width:24px;height:24px}

/* hero */
.hero{position:absolute;left:0;top:0;width:1200px;height:610px}
.hero-photo{position:absolute;inset:0;background:linear-gradient(160deg,#9fb1c6 0%,#5d7391 45%,#8ea3bb 75%,#c4d0dd 100%)}
.hero-copy{position:absolute;left:0;top:250px;width:1200px;text-align:center;color:#fff}
.hero-copy h1{font-size:32px;font-weight:700;line-height:1.5;letter-spacing:.06em;text-shadow:0 2px 6px rgba(20,40,70,.5)}
.hero-copy p{margin-top:30px;font-size:15px;letter-spacing:.08em;opacity:.9}
.hero-btn{position:absolute;left:520px;top:404px;width:160px;height:40px;border:1px solid #fff;background:rgba(255,255,255,.15);color:#fff;font-size:14px;display:flex;align-items:center;justify-content:center;letter-spacing:.1em}

/* section titles */
.sec-title{position:absolute;width:184px;height:46px;left:508px;border:3px double var(--steel);background:#fff;display:flex;align-items:center;justify-content:center;font-size:20px;font-weight:700;color:var(--navy);letter-spacing:.08em}

/* strengths */
.strengths{position:absolute;left:184px;top:632px;width:832px;height:572px;background:var(--pale);border:1px solid var(--line)}
.strengths-inner{position:absolute;left:14px;top:14px;width:802px;height:542px;background:#fff}
.strengths-lead{position:absolute;left:230px;top:100px;width:360px;font-size:11px;line-height:1.9;color:var(--muted)}
.point{position:absolute;top:200px;width:220px;text-align:center}
.point-circle{margin:0 auto;width:118px;height:118px;border-radius:50%;border:6px solid #d7dde5;background:#fff;position:relative;display:flex;align-items:center;justify-content:center;color:var(--red);font-weight:700;font-size:19px;line-height:1.25}
.point-tag{position:absolute;left:34px;top:-16px;width:38px;height:38px;border-radius:50%;background:var(--navy);color:#fff;font-size:9px;display:flex;align-items:center;justify-content:center}
.point p{margin-top:36px;font-size:10px;line-height:1.8;color:var(--muted);text-align:left;padding:0 8px}
.point-photo{position:absolute;top:438px;width:168px;height:84px;background:linear-gradient(135deg,#54657a,#a8b6c6 60%,#7b8a9b)}

/* works */
.works{position:absolute;left:0;top:1226px;width:1200px;height:400px;background:var(--gray)}
.works-lead{position:absolute;left:300px;top:160px;width:600px;text-align:center;font-size:11px;line-height:1.8;color:var(--muted)}
.work-photo{position:absolute;top:228px;width:176px;height:108px;background:linear-gradient(135deg,#c08a56 0%,#e7c9a5 40%,#8a9aa8 100%);box-shadow:0 3px 8px rgba(0,0,0,.18)}

/* news */
.news{position:absolute;left:0;top:1660px;width:1200px;height:990px;background:#dde4ec}
.news-item{position:absolute;left:272px;width:656px;height:128px}
.news-photo{position:absolute;left:0;top:0;width:180px;height:128px;background:linear-gradient(150deg,#3c4e63,#9a7a5c 55%,#c9d2dc)}
.news-body{position:absolute;left:184px;top:0;width:472px;height:128px;background:#fff;border-right:6px solid #f0c2b8;padding:14px 20px}
.news-body time{font-size:11px;color:var(--muted)}
.news-body h3{font-size:12px;color:var(--blue);margin:4px 0 8px;font-weight:700}
.news-body p{font-size:10px;line-height:1.8;color:var(--muted)}

/* recruit */
.recruit{position:absolute;left:0;top:2660px;width:1200px;height:340px;background:#fff}
.recruit-banner{position:absolute;left:184px;top:186px;width:832px;height:140px;background:linear-gradient(120deg,#4c6a8e,#8ea7c2 50%,#5a7598);border:6px solid var(--pale)}
.recruit-copy{position:absolute;left:420px;top:26px;color:#fff;font-size:17px;line-height:1.5;font-weight:500;letter-spacing:.05em}
.recruit-more{position:absolute;right:18px;bottom:10px;color:#fff;font-size:10px}

/* footer */
.site-footer{position:absolute;left:0;top:3008px;width:1200px;height:308px;background:#f5f6f8;border-top:14px solid var(--steel)}
.foot-brand{position:absolute;left:188px;top:72px;width:94px;height:80px;border:1px solid var(--navy);display:flex;flex-direction:column;align-items:center;justify-content:center;gap:6px;font-size:12px;color:var(--navy);font-weight:500}
.foot-brand i{width:12px;height:12px;background:var(--navy);display:block}
.foot-links{position:absolute;top:60px;font-size:10px;line-height:2.1;color:var(--muted);list-style:none}
.foot-info{position:absolute;left:790px;top:60px;font-size:10px;line-height:1.9;color:var(--muted)}
.foot-map{position:absolute;left:790px;top:112px;width:120px;height:80px;background:linear-gradient(135deg,#e8e6de,#d4dbe2)}
.copyright{position:absolute;left:0;bottom:14px;width:1200px;text-align:center;font-size:10px;color:var(--muted)}
</style>
</head>
<body>

<section class="hero">
  <div class="hero-photo" role="img" aria-label="鉄骨階段と構造体を見上げた写真"></div>
  <div class="hero-copy">
    <h1>鉄を極め、究極の階段づくりを通して<br>建設業界の支援に寄与し、社会に貢献します。</h1>
    <p>鉄骨階段の設計・製作・施工まで一貫して対応いたします</p>
  </div>
  <div class="hero-btn">お見積りはこちら</div>
</section>

<header class="site-header">
  <div class="brand"><span>三海鉄工</span></div>
  <div class="brand-sub">SANKAI</div>
  <div class="tel">000-0000-0000</div>
  <nav class="global-nav">
    <a href="#"><svg viewBox="0 0 24 24"><path d="M3 11 12 3l9 8v10h-6v-6H9v6H3z" fill="#1f3f6b"/></svg>HOME</a>
    <a href="#"><svg viewBox="0 0 24 24"><rect x="4" y="3" width="16" height="18" fill="#1f3f6b"/><rect x="8" y="7" width="3" height="3" fill="#fff"/><rect x="13" y="7" width="3" height="3" fill="#fff"/><rect x="8" y="13" width="3" height="3" fill="#fff"/><rect x="13" y="13" width="3" height="3" fill="#fff"/></svg>会社概要</a>
    <a href="#"><svg viewBox="0 0 24 24"><rect x="3" y="7" width="18" height="13" fill="#1f3f6b"/><rect x="9" y="4" width="6" height="4" fill="none" stroke="#1f3f6b" stroke-width="2"/></svg>事業案内</a>
    <a href="#"><svg viewBox="0 0 24 24"><circle cx="12" cy="12" r="8" fill="#1f3f6b"/><circle cx="12" cy="12" r="3" fill="#fff"/></svg>設備紹介</a>
    <a href="#"><svg viewBox="0 0 24 24"><path d="M3 20h18M5 20V14h4v-4h4V6h4v14" fill="none" stroke="#1f3f6b" stroke-width="2.5"/></svg>施工実績</a>
    <a href="#"><svg viewBox="0 0 24 24"><path d="M3 4h18v12H9l-5 4v-4H3z" fill="#1f3f6b"/></svg>ブログ</a>
    <a href="#"><svg viewBox="0 0 24 24"><circle cx="12" cy="8" r="4" fill="#1f3f6b"/><path d="M4 21c0-5 4-7 8-7s8 2 8 7z" fill="#1f3f6b"/></svg>採用情報</a>
    <a href="#"><svg viewBox="0 0 24 24"><rect x="3" y="5" width="18" height="14" fill="#1f3f6b"/><path d="M3 5l9 8 9-8" fill="none" stroke="#fff" stroke-width="1.5"/></svg>お問い合わせ</a>
  </nav>
</header>

<section class="strengths">
  <div class="strengths-inner">
    <div class="sec-title" style="left:310px;top:14px">我が社の強み</div>
    <p class="strengths-lead">当社は創業以来、鉄骨階段一筋に技術を磨いてまいりました。設計から製作、施工までを自社で行うことで、高品質かつ短納期のものづくりを実現しています。確かな技術で建設業界を支えます。</p>
    <div class="point" style="left:40px">
      <div class="point-circle"><span class="point-tag">強み1</span>一貫製造<br>施工</div>
      <p>設計・製作・施工までを自社で一貫して行い、品質と納期を確実にお約束します。</p>
    </div>
    <div class="point" style="left:291px">
      <div class="point-circle"><span class="point-tag">強み2</span>数多くの<br>実績</div>
      <p>これまでに手がけた階段は多数。様々な現場で培った経験が強みです。</p>
    </div>
    <div class="point" style="left:542px">
      <div class="point-circle"><span class="point-tag">強み3</span>人材育成</div>
      <p>職人の技を次世代へ。社内教育に力を入れ、確かな技術を受け継ぎます。</p>
    </div>
    <div class="point-photo" role="img" aria-label="工場での製作作業の写真" style="left:66px"></div>
    <div class="point-photo" role="img" aria-label="施工した鉄骨階段の写真" style="left:317px"></div>
    <div class="point-photo" role="img" aria-label="職人の作業風景の写真" style="left:568px"></div>
  </div>
</section>

<section class="works">
  <div class="sec-title" style="top:94px">施行実績</div>
  <p class="works-lead">これまでに施工した鉄骨階段の一部をご紹介します。<br>住宅から商業施設まで、幅広い現場に対応しております。</p>
  <div class="work-photo" role="img" aria-label="施工事例の屋外階段の写真" style="left:212px"></div>
  <div class="work-photo" role="img" aria-label="施工事例の屋外階段の写真" style="left:412px"></div>
  <div class="work-photo" role="img" aria-label="施工事例の屋外階段の写真" style="left:612px"></div>
  <div class="work-photo" role="img" aria-label="施工事例の屋外階段の写真" style="left:812px"></div>
</section>

<section class="news">
  <div class="sec-title" style="top:110px">新着情報</div>
  <article class="news-item" style="top:190px">
    <div class="news-photo" role="img" aria-label="鉄骨階段の写真"></div>
    <div class="news-body"><time>2015.00.15</time><h3>新着情報のタイトルが入ります</h3><p>ここに新着情報の本文が入ります。社内の動きや施工の様子などをお知らせします。ここに本文が入ります。</p></div>
  </article>
  <article class="news-item" style="top:386px">
    <div class="news-photo" role="img" aria-label="鉄骨階段の写真"></div>
    <div class="news-body"><time>2015.00.15</time><h3>新着情報のタイトルが入ります</h3><p>ここに新着情報の本文が入ります。社内の動きや施工の様子などをお知らせします。ここに本文が入ります。</p></div>
  </article>
  <article class="news-item" style="top:582px">
    <div class="news-photo" role="img" aria-label="鉄骨階段の写真"></div>
    <div class="news-body"><time>2015.00.15</time><h3>新着情報のタイトルが入ります</h3><p>ここに新着情報の本文が入ります。社内の動きや施工の様子などをお知らせします。ここに本文が入ります。</p></div>
  </article>
  <article class="news-item" style="top:778px">
    <div class="news-photo" role="img" aria-label="鉄骨階段の写真"></div>
    <div class="news-body"><time>2015.00.15</time><h3>新着情報のタイトルが入ります</h3><p>ここに新着情報の本文が入ります。社内の動きや施工の様子などをお知らせします。ここに本文が入ります。</p></div>
  </article>
</section>

<section class="recruit">
  <div class="sec-title" style="top:60px">採用情報</div>
  <div class="recruit-banner" role="img" aria-label="鉄骨構造を見上げた写真のバナー">
    <p class="recruit-copy">未来の階段づくりを担う仲間を<br>募集しています。確かな技術を<br>一緒に磨いていきませんか。</p>
    <span class="recruit-more">詳しくはこちら</span>
  </div>
</section>

<footer class="site-footer">
  <div class="foot-brand"><i></i>三海鉄工</div>
  <ul class="foot-links" style="left:330px"><li>HOME</li><li>会社概要</li><li>ブログ</li></ul>
  <ul class="foot-links" style="left:430px"><li>事業案内</li><li>スタッフ紹介</li><li>施工実績</li><li>設備紹介</li></ul>
  <ul class="foot-links" style="left:550px"><li>採用情報</li><li>求人案内</li><li>先輩の声</li></ul>
  <ul class="foot-links" style="left:660px"><li>お問い合わせ</li><li>見積り</li><li>アクセス</li></ul>
  <div class="foot-info">TEL 000-0000-0000<br>FAX 000-0000-0001</div>
  <div class="foot-map" role="img" aria-label="所在地の地図"></div>
  <p class="copyright">Copyright © 三海鉄工 All Rights Reserved.</p>
</footer>

</body>
</html>
```